"A Touch RMB" Business Card/Logo Design

I'm looking for a very creative look for my new business called "A Touch RMB" on a business card design. Don't be distracted by my "business card details" below....if you have other ideas on how you see "A Touch RMB" go for it. If probably should somehow give a look that I paint furniture....maybe a paint drip or something simple or you can get more creative....sky's the limit and I really need your creative eye on how to per tray that "A Touch RMB" means taking something old and turning into new again with some paint.

Industry/Entity Type

Business

Contact Information for Business Card

I refurbish and up-cycle furniture that needs "a little TLC'....thus, my business name was born called "A Touch RMB" (Those are my initials). I mainly paint old furniture of all styles and bring them back to life. I sometimes recreate furniture as well....I will make benches from old headboards of all sizes, etc. I'd love to see design that incorporate the crafty/creative side of me. If that means incorporating a paint brush, tools, paint cans, or furniture such as dressers, old vintage furniture, spindles, etc, etc. I don't know if something creative could be done with my initials (RMB). I really have a creative block of ideas and need your help bringing my "A Touch RMB" business to life.

P.S. Below is just one picture that I thought was neat and creative as they used a paintbrush but used spindles for the bristles and put their logo in the middle. Just an idea I thought was very unique and creative.

I'm very excited to see your design. Thank you for taking the time to create my logo/business card for me.

Carla

Requirements
Must have
• Please include this information on the card:
• My Name: Carla Brennick
• Address: 14706 318th Ln SE, Fox Hollow, MN 55418
• E-Mail: atouchrmb@mailcove.net
• FB: http:/www.friendpage.net/atouchrmb
• Cell: 763-419-7082

```html
<!DOCTYPE html>
<html lang="en">
<head>
<meta charset="utf-8">
<title>A Touch RMB – Business Card</title>
<link rel="stylesheet" href="https://fonts.googleapis.com/css2?family=Josefin+Sans:wght@600&family=Oswald:wght@400;500&display=swap">
<style>
  :root {
    --page: #f3f3f1;
    --card-deep: #3f63c4;
    --card-mid: #4a78d3;
    --card-light: #6d8fd8;
    --card-violet: #5a62bf;
    --ink-light: #ffffff;
    --mark-blue: #8ea6de;
  }
  * { margin: 0; padding: 0; box-sizing: border-box; }
  html, body { width: 1200px; height: 1000px; overflow: hidden; }
  body {
    background: var(--page);
    font-family: "Oswald", sans-serif;
    position: relative;
  }
  .card {
    position: absolute;
    width: 400px;
    height: 640px;
    top: 180px;
    border-radius: 4px;
    overflow: hidden;
    box-shadow: 0 6px 18px rgba(40, 60, 110, 0.18);
  }
  .card--back { left: 150px; }
  .card--front { left: 650px; }
  .card__wash {
    position: absolute;
    inset: 0;
    display: block;
  }
  .card--back .card__wash {
    background:
      radial-gradient(ellipse 60% 40% at 30% 20%, rgba(255,255,255,0.18), transparent 70%),
      radial-gradient(ellipse 70% 50% at 70% 80%, var(--card-violet), transparent 75%),
      linear-gradient(170deg, var(--card-light), var(--card-deep));
  }
  .card--front .card__wash {
    background:
      radial-gradient(ellipse 55% 30% at 50% 22%, rgba(255,255,255,0.16), transparent 75%),
      radial-gradient(ellipse 60% 55% at 35% 75%, var(--card-mid), transparent 80%),
      linear-gradient(175deg, var(--card-deep), var(--card-violet) 55%, var(--card-mid));
  }
  .card__content {
    position: relative;
    height: 100%;
    display: flex;
    flex-direction: column;
    align-items: center;
    color: var(--ink-light);
    text-align: center;
  }
  .brand {
    margin-top: 110px;
    font-family: "Oswald", sans-serif;
    font-weight: 500;
    font-size: 52px;
    line-height: 1;
    letter-spacing: 1px;
  }
  .brand-tagline {
    margin-top: 26px;
    font-size: 14px;
    letter-spacing: 4px;
    text-transform: uppercase;
  }
  .owner-name {
    margin-top: 110px;
    font-family: "Josefin Sans", sans-serif;
    font-weight: 600;
    font-size: 34px;
    letter-spacing: 3px;
    text-transform: uppercase;
  }
  .contact {
    margin-top: 34px;
    list-style: none;
    font-size: 17px;
    line-height: 1.45;
  }
  .standalone-mark {
    position: absolute;
    left: 1080px;
    top: 0;
  }
</style>
</head>
<body>
  <section class="card card--back" aria-label="Card back">
    <div class="card__wash" role="img" aria-label="Blue watercolour wash background"></div>
  </section>

  <section class="card card--front" aria-label="Card front">
    <div class="card__wash" role="img" aria-label="Blue watercolour wash background"></div>
    <div class="card__content">
      <p class="brand">A Touch RMB</p>
      <p class="brand-tagline">Furniture Restoration</p>
      <h1 class="owner-name">Carla Brennick</h1>
      <ul class="contact">
        <li>14706 318th Ln SE, Fox Hollow, MN 55418</li>
        <li>E-Mail: atouchrmb@mailcove.net</li>
        <li>FB: http:/www.friendpage.net/atouchrmb</li>
        <li>Cell: 763-419-7082</li>
      </ul>
    </div>
  </section>
</body>
</html>
```